We need a book cover design for a handbook related to the implementation of new European privacy regulation. The topic is quite technical but the goal is to have something actionnable for small businesses and small non-profit organizations. It's really a handbook that should inspire confidence for the managers who have to be compliant in a pragmatic way (not like big corporate structures). The final format should be in PDF with specific requirements to be publish on PrintKettle.com.

Title: QLTA Playbook for small firms
Subtitle: Get set in 14 weeks (or fewer)
Author: Bertrand Molineux
Edition: 1.0
ISBN-13: 978-1555038210
ISBN-10: 1555038217

The book has a size of 6" x 9" and is composed by 52 pages.
Spine width should be 52 x 0.002252 = 0,117104"
Additional technical info in the attachments.

For text and inspiration about the covers (rear cover especially), please use the text on https://www.qlta-playbook.eu.

Feel free to ask questions to clarify some aspects!

Target Market(s)

Managing Directors of small businesses

Industry/Entity Type

Technical

Colors

Designer to choose colors to be used in the design.

Requirements
Must have
• - Inspire confidence and accessibility (simple, easy, time effective)
• - Title, subtitle and author on the front cover
• - ISBNs, barcode and mention "Templates available on https://www.qlta-playbook.eu" + text coming from the website
Nice to have
• - Simplicity
• - Easy path to compliance, shortcut
• - Time saving
Should not have
• - Picture of the author
• - Text on the spine

```html
<!DOCTYPE html>
<html lang="en">
<head>
<meta charset="utf-8">
<title>QLTA Playbook for small firms — Front Cover</title>
<link rel="stylesheet" href="https://fonts.googleapis.com/css2?family=Arvo:wght@400;700&family=Gochi+Hand&family=Cormorant+SC:wght@600&display=swap">
<style>
  :root {
    --stage: #e4e4e6;
    --cover-blue: #333a8c;
    --cover-blue-light: #3c4499;
    --panel-navy: #1a1d63;
    --panel-navy-top: #23287a;
    --title-ink: #e4e6f5;
    --accent-yellow: #f5cf22;
    --tagline-ink: #1b1b2e;
    --author-ink: #ffffff;
    --wave-tint: rgba(120, 130, 215, 0.35);
  }
  * { box-sizing: border-box; margin: 0; padding: 0; }
  html, body {
    width: 1200px;
    height: 927px;
    overflow: hidden;
    background: var(--stage);
  }
  .book-cover {
    position: absolute;
    left: 326px;
    top: 52px;
    width: 548px;
    height: 822px;
    background: linear-gradient(180deg, var(--cover-blue-light) 0%, var(--cover-blue) 60%, var(--cover-blue) 100%);
    overflow: hidden;
    box-shadow: 0 10px 30px rgba(0, 0, 0, 0.25);
  }
  .wave-field {
    position: absolute;
    left: 0;
    top: 270px;
    width: 100%;
    height: 440px;
    background:
      radial-gradient(ellipse 60% 30% at 70% 20%, var(--wave-tint), transparent 70%),
      radial-gradient(ellipse 70% 35% at 30% 60%, var(--wave-tint), transparent 70%),
      radial-gradient(ellipse 80% 25% at 60% 85%, rgba(120, 130, 215, 0.2), transparent 70%);
  }
  .title-panel {
    position: absolute;
    left: 66px;
    top: 0;
    right: 0;
    height: 262px;
    background: linear-gradient(180deg, var(--panel-navy-top) 0%, var(--panel-navy) 100%);
    border-bottom-left-radius: 16px;
    text-align: right;
    padding: 20px 30px 0 0;
  }
  .title-main {
    font-family: "Arvo", serif;
    font-weight: 700;
    font-size: 108px;
    line-height: 1;
    color: var(--title-ink);
    letter-spacing: 1px;
  }
  .title-sub {
    font-family: "Arvo", serif;
    font-weight: 700;
    font-size: 44px;
    line-height: 1;
    color: var(--title-ink);
    letter-spacing: 5px;
    margin-top: 2px;
  }
  .title-audience {
    font-family: "Arvo", serif;
    font-weight: 400;
    font-size: 40px;
    line-height: 1.1;
    color: var(--accent-yellow);
    margin-top: 8px;
  }
  .tagline-band {
    position: absolute;
    left: 88px;
    right: 0;
    top: 246px;
    height: 48px;
    background: var(--accent-yellow);
    border-top-left-radius: 8px;
    border-bottom-left-radius: 8px;
    display: flex;
    align-items: center;
    padding-left: 20px;
  }
  .tagline {
    font-family: "Gochi Hand", cursive;
    font-size: 28px;
    color: var(--tagline-ink);
    letter-spacing: 0.5px;
  }
  .author {
    position: absolute;
    left: 150px;
    top: 708px;
    font-family: "Cormorant SC", serif;
    font-weight: 600;
    font-size: 34px;
    letter-spacing: 3px;
    color: var(--author-ink);
  }
</style>
</head>
<body>
  <main class="book-cover">
    <div class="wave-field" role="img" aria-label="Flowing mesh of fine light-blue wave lines across the lower cover"></div>
    <header class="title-panel">
      <h1 class="title-main">QLTA</h1>
      <p class="title-sub">PLAYBOOK</p>
      <p class="title-audience">for small firms</p>
    </header>
    <div class="tagline-band">
      <p class="tagline">Get set in 14 weeks (or fewer)</p>
    </div>
    <p class="author">Bertrand Molineux</p>
  </main>
</body>
</html>
```